Letterhead & Business Card Design Project

Use existing logo to create a new letterhead and business card design. Looking for something clean modern using color options of black, white and gray. The green from the logo may be used lightly as an accent color.

Target Market(s)

Professional business people

Industry/Entity Type

Business

Requirements
Must have
• Business card with front and back design using existing logo.
Nice to have
• Professional presentation
Clean look
Should not have
• No oil rigs, pumpjacks or clip art.

```html
<!DOCTYPE html>
<html lang="en">
<head>
<meta charset="utf-8">
<title>Halvern Resources — Letterhead &amp; Business Card</title>
<link rel="stylesheet" href="https://fonts.googleapis.com/css2?family=Tinos:wght@400;700&display=swap">
<style>
  :root {
    --backdrop: #efeedb;
    --paper: #ffffff;
    --ink: #1d1d1d;
    --ink-soft: #555555;
    --band-gray: #cfcfd0;
    --accent-green: #7fba6a;
    --accent-line: #9ccc86;
  }
  * { margin: 0; padding: 0; box-sizing: border-box; }
  html, body {
    width: 1200px; height: 1142px; overflow: hidden;
    background: var(--backdrop);
    font-family: "Tinos", "Times New Roman", serif;
    color: var(--ink);
  }
  .canvas { position: relative; width: 1200px; height: 1142px; }

  /* Letterhead */
  .letterhead {
    position: absolute; left: 347px; top: 193px;
    width: 544px; height: 769px;
    background: var(--paper);
  }
  .letterhead .brand-name {
    position: absolute; left: 0; right: 0; top: 30px;
    text-align: center;
    font-size: 24px; letter-spacing: 1.5px; color: var(--ink);
    line-height: 28px; white-space: nowrap;
  }
  .letterhead .brand-rule {
    position: absolute; left: 182px; width: 180px; top: 62px;
    height: 1px; background: var(--accent-line);
  }
  .letterhead .address, .letterhead .contact {
    position: absolute; top: 50px;
    font-size: 7px; line-height: 16px; color: var(--ink-soft);
    white-space: nowrap;
  }
  .letterhead .address { left: 57px; }
  .letterhead .contact { right: 58px; text-align: right; }
  .letterhead .footer-band {
    position: absolute; left: 0; right: 0; bottom: 0; height: 30px;
    background: var(--band-gray);
    display: flex; align-items: center; justify-content: center;
    font-size: 9px; font-weight: 700; color: var(--ink);
  }

  /* Business card front */
  .card { position: absolute; left: 768px; width: 190px; }
  .card-front { top: 352px; height: 106px; background: var(--paper); }
  .card-front .name-band {
    position: absolute; left: 0; top: 0; width: 190px; height: 42px;
    background: var(--band-gray);
  }
  .card-front .person {
    position: absolute; left: 13px; top: 9px;
    font-size: 8px; line-height: 10px; color: var(--ink); white-space: nowrap;
  }
  .card-front .title {
    position: absolute; left: 13px; top: 23px;
    font-size: 5px; line-height: 7px; color: var(--ink); white-space: nowrap;
  }
  .card-front .brand-name {
    position: absolute; left: 50px; width: 128px; top: 48px;
    text-align: center;
    font-size: 11px; line-height: 13px; letter-spacing: 0.6px; color: var(--ink);
    white-space: nowrap;
  }
  .card-front .brand-rule {
    position: absolute; left: 68px; width: 92px; top: 64px;
    height: 1px; background: var(--accent-line);
  }
  .card-front .details {
    position: absolute; left: 49px; right: 12px; top: 82px;
    font-size: 5px; line-height: 9px; color: var(--ink-soft); white-space: nowrap;
  }
  .card-front .details .row { display: flex; justify-content: space-between; }

  /* Business card back */
  .card-back { top: 486px; height: 107px; background: var(--accent-green); }
  .card-back .web-line { position: absolute; left: 0; top: 48px; width: 190px; height: 14px; }
  .card-back .web {
    position: absolute; left: 0; right: 0; top: 49px;
    text-align: center; font-size: 5.5px; font-weight: 700; color: var(--ink);
  }
</style>
</head>
<body>
<main class="canvas">
  <section class="letterhead" aria-label="Letterhead">
    <div class="brand-name">Halvern Resources</div>
    <div class="brand-rule"></div>
    <div class="address">4412 East Brook Ave Suite<br>210 Tulsa, Oklahoma 74135</div>
    <div class="contact">Phone 918.555.0142<br>Fax 918.555.0143</div>
    <div class="footer-band">www.halvernresources.com</div>
  </section>

  <section class="card card-front" aria-label="Business card front">
    <div class="name-band"></div>
    <div class="person">Daniel R Whitford</div>
    <div class="title">Managing Member<br>cell 918.555.0178</div>
    <div class="brand-name">Halvern Resources</div>
    <div class="brand-rule"></div>
    <div class="details">
      <div>4412 East Brook Ave Suite 210 Tulsa, Oklahoma 74135</div>
      <div class="row"><span>Phone 918.555.0142</span><span>Fax 918.555.0143</span></div>
    </div>
  </section>

  <section class="card card-back" aria-label="Business card back">
    <svg class="web-line" viewBox="0 0 190 14" aria-hidden="true">
      <defs>
        <linearGradient id="fade" x1="0" x2="1">
          <stop offset="0" stop-color="#ffffff" stop-opacity="0"/>
          <stop offset="0.5" stop-color="#ffffff" stop-opacity="0.9"/>
          <stop offset="1" stop-color="#ffffff" stop-opacity="0"/>
        </linearGradient>
      </defs>
      <rect x="28" y="6" width="134" height="1" fill="url(#fade)"/>
    </svg>
    <div class="web">www.halvernresources.com</div>
  </section>
</main>
</body>
</html>
```